Principal Licensure: BRL Cohort

I am writing to you from the office of Extended & Career Studies within the Faculty of Teaching & Learner Growth at the Halvern Ridge University. We offer professional education and learning opportunities to educators in Colorado. We are looking for a brochure design for our new program that prepares aspiring leaders to apply for principal licensure to become a school principal. The program is called the "BRL Cohort." We are partnering with Brellow Regional Learning (http://www.guidebrellow.example/) to offer the program. Both of our organizations value innovation, urban schools and school reform. The final design should communicate leadership, equity and diversity and thinking outside of the box. Unfortunately, we do not have any images on hand so we welcome any image proposals. Images should reflect ethnic, age, and gender diversity. Images should include professionals that are interacting with students (adult or children) or with one another in an educational and collaborative setting.
Is there any way to design the brochure so it may be sent via email as well?

Hi everyone! I posted a couple more logos in case they might be a better fit for the designs. Thanks!
Tessa

Target Market(s)

Educators and business professionals 30-45 years old who are passionate about urban schools and education reform.

Industry/Entity Type

Education

Requirements
Must have
• The brochure must include all text that is attached. I have attached a few of our other pieces to give you an idea of what we already work with. We would like this one to look associated but also have a distinct look, tailored to professionals. We really like the arrow and the color bar that is a part of our header (see attached brochure) It should also include the HRU and BRL logos (also attached). We are not committed to particular colors but I have attached a color palette.
Should not have
• It should not include overplayed education images such as apples, chalkboards, students sitting in desks with their hands raised. We want to convey a collaborative approach that attracts leaders and business professionals. We are looking for color and something different than the standard education imagery.

```html
<!DOCTYPE html>
<html lang="en">
<head>
<meta charset="utf-8">
<title>Principal Licensure: BRL Cohort brochure</title>
<link rel="stylesheet" href="https://fonts.googleapis.com/css2?family=Roboto:ital,wght@0,300;0,400;0,700;1,300&family=Roboto+Condensed:wght@700&display=swap">
<style>
  :root {
    --green: #8cc63f;
    --orange: #f7a823;
    --blue: #1e9ad6;
    --teal: #2aa9c9;
    --lime: #d7df23;
    --sky: #c4e5f4;
    --ink: #333;
    --body: #5e5e5e;
    --rule: #9a9a9a;
    --frame: #b8b8b8;
    --bar-1: #e8792b;
    --bar-2: #d04a26;
    --bar-3: #c3b58a;
    --bar-4: #1f5a8a;
    --bar-5: #7d7d7d;
    --bar-6: #9acd3c;
    --bar-7: #a8d8ea;
    --bar-8: #e0a93a;
  }
  * { box-sizing: border-box; margin: 0; padding: 0; }
  html, body { width: 881px; height: 1200px; overflow: hidden; background: #fff; }
  body { font-family: "Roboto", Arial, sans-serif; font-weight: 300; color: var(--body); }
  .canvas { position: relative; width: 881px; height: 1200px; background: #fff; }

  .page { position: absolute; width: 418px; height: 576px; border: 1px solid var(--frame); background: #fff; overflow: hidden; }
  .page--back { left: 14px; top: 12px; }
  .page--cover { left: 446px; top: 12px; }
  .page--inside-left { left: 14px; top: 617px; }
  .page--inside-right { left: 450px; top: 617px; }

  .color-bar { position: absolute; left: 0; top: 0; width: 100%; height: 8px; display: flex; z-index: 3; }
  .color-bar span { flex: 1; }
  .color-bar span:nth-child(8n+1) { background: var(--bar-1); }
  .color-bar span:nth-child(8n+2) { background: var(--bar-2); }
  .color-bar span:nth-child(8n+3) { background: var(--bar-3); }
  .color-bar span:nth-child(8n+4) { background: var(--bar-4); }
  .color-bar span:nth-child(8n+5) { background: var(--bar-5); }
  .color-bar span:nth-child(8n+6) { background: var(--bar-6); }
  .color-bar span:nth-child(8n+7) { background: var(--bar-7); }
  .color-bar span:nth-child(8n+8) { background: var(--bar-8); }

  .web-address { position: absolute; bottom: 13px; font-size: 6.6px; font-weight: 400; color: var(--ink); }
  .web-address--right { right: 24px; }
  .web-address--left { left: 19px; }

  .bottom-swoosh { position: absolute; left: 0; bottom: 0; width: 100%; height: 40px; }

  /* wordmarks */
  .unit-mark { position: absolute; display: flex; align-items: center; gap: 5px; font-size: 7.4px; font-weight: 400; color: var(--ink); }
  .unit-mark i { display: block; width: 13px; height: 13px; background: var(--ink); }
  .partner-mark { position: absolute; display: flex; align-items: center; gap: 5px; width: 84px; font-size: 7px; line-height: 8px; font-weight: 400; color: var(--blue); }
  .partner-mark i { display: block; flex: none; width: 20px; height: 20px; border: 1.2px solid var(--blue); }

  /* back page */
  .note-lines { position: absolute; left: 46px; top: 74px; width: 304px; }
  .note-lines li { list-style: none; height: 18.5px; border-top: 0.8px solid var(--rule); }
  .back-tab { position: absolute; left: 0; top: 456px; width: 222px; height: 14px; background: var(--orange); clip-path: polygon(0 0, 212px 0, 222px 14px, 0 14px); font-size: 8px; line-height: 14px; padding-left: 45px; color: var(--ink); font-weight: 400; }
  .contact { position: absolute; left: 133px; top: 478px; font-size: 6.2px; line-height: 8.2px; color: var(--ink); font-style: normal; }

  /* cover */
  .cover-art { position: absolute; left: 0; top: 8px; width: 418px; height: 440px; }
  .cover-mark { left: 237px; top: 36px; z-index: 2; }
  .cover-mark { color: var(--ink); }
  .cover-headline { position: absolute; left: 0; top: 375px; width: 418px; font-family: "Roboto Condensed", "Arial Narrow", sans-serif; font-weight: 700; font-size: 30px; line-height: 31px; letter-spacing: -0.8px; }
  .cover-headline span { display: block; }
  .cover-headline .line-1 { padding-left: 20px; color: var(--green); }
  .cover-headline .line-2 { padding-left: 36px; color: var(--orange); }
  .cover-headline .line-3 { padding-left: 156px; color: var(--blue); }
  .cover-subtitle { position: absolute; left: 161px; top: 472px; font-size: 13px; color: #444; }
  .cover-partner { left: 318px; top: 523px; }

  /* inside pages */
  .tab { position: absolute; left: 0; height: 14px; font-size: 9.5px; line-height: 14px; font-weight: 400; color: var(--ink); padding-left: 79px; }
  .tab--green { background: var(--green); }
  .tab--orange { background: var(--orange); }
  .tab { clip-path: polygon(0 0, calc(100% - 9px) 0, 100% 14px, 0 14px); }

  .copy { position: absolute; left: 79px; width: 284px; font-size: 5.9px; line-height: 8.1px; }
  .copy p + p { margin-top: 5px; }
  .page--inside-right .copy { width: 206px; }

  .dot-arrow { position: absolute; width: 26px; height: 16px; }
  .dot-arrow--small { width: 18px; height: 11px; }

  .callout { position: absolute; left: 79px; top: 483px; width: 284px; font-size: 7.9px; line-height: 10.4px; font-style: italic; color: var(--blue); font-weight: 300; }

  .sessions { position: absolute; left: 79px; top: 167px; width: 206px; height: 82px; background: var(--lime); padding: 5px 6px 0 6px; list-style: none; }
  .sessions li { position: relative; padding-left: 12px; font-size: 5.8px; line-height: 7.4px; color: var(--ink); margin-bottom: 5px; }
  .sessions li::before { content: ""; position: absolute; left: 1px; top: 1.6px; width: 3.6px; height: 3.6px; background: var(--blue); transform: rotate(45deg); }
  .sessions b { font-weight: 700; }

  .price { position: absolute; left: 79px; top: 459px; font-size: 5.9px; line-height: 8px; color: var(--ink); }
  .price strong { font-size: 12px; font-weight: 300; }

  .info-box { position: absolute; left: 25px; top: 502px; width: 258px; height: 40px; border: 0.8px solid var(--orange); padding: 3px 5px; }
  .info-box h3 { font-size: 9.5px; font-weight: 400; color: var(--ink); line-height: 11px; }
  .info-box p { font-size: 5.8px; line-height: 7.6px; }

  .apply { position: absolute; left: 294px; top: 53px; width: 124px; height: 484px; background: var(--sky); padding: 6px 6px 0 10px; font-size: 5.7px; line-height: 7.7px; }
  .apply h2 { font-size: 15.5px; font-weight: 300; color: var(--ink); line-height: 20px; margin-bottom: 4px; }
  .apply p { margin-bottom: 6px; }
  .apply b { font-weight: 700; color: var(--ink); }
  .apply ul { list-style: none; margin: 2px 0 8px -7px; }
  .apply li { display: flex; align-items: center; gap: 5px; height: 13px; }
  .apply li svg { width: 10px; height: 7px; flex: none; }
  .apply .link { word-break: break-all; }
</style>
</head>
<body>
<svg width="0" height="0" style="position:absolute" aria-hidden="true">
  <defs>
    <symbol id="dot-arrow" viewBox="0 0 26 16">
      <circle cx="2" cy="8" r="1.3"/><circle cx="6" cy="8" r="1.3"/><circle cx="10" cy="8" r="1.3"/>
      <circle cx="14" cy="8" r="1.3"/><circle cx="18" cy="8" r="1.3"/><circle cx="22.5" cy="8" r="1.3"/>
      <circle cx="19" cy="4.2" r="1.3"/><circle cx="15.5" cy="1.4" r="1.3"/>
      <circle cx="19" cy="11.8" r="1.3"/><circle cx="15.5" cy="14.6" r="1.3"/>
    </symbol>
    <symbol id="line-arrow" viewBox="0 0 10 7">
      <path d="M0 3.5 H9 M6 0.6 L9 3.5 L6 6.4" fill="none" stroke="#fff" stroke-width="0.9"/>
    </symbol>
  </defs>
</svg>

<main class="canvas">

  <!-- Back cover -->
  <section class="page page--back">
    <div class="color-bar"><span></span><span></span><span></span><span></span><span></span><span></span><span></span><span></span><span></span><span></span><span></span><span></span><span></span><span></span><span></span><span></span></div>
    <div class="unit-mark" style="left:12px;top:26px;"><i></i>Extended &amp; Career Studies</div>
    <ul class="note-lines">
      <li></li><li></li><li></li><li></li><li></li><li></li><li></li><li></li><li></li><li></li>
      <li></li><li></li><li></li><li></li><li></li><li></li><li></li><li></li><li></li>
    </ul>
    <div class="back-tab">Extended &amp; Career Studies</div>
    <div class="partner-mark" style="left:48px;top:484px;"><i></i>Brellow Regional Learning</div>
    <address class="contact">
      Contact<br>
      Halvern Ridge University<br>
      Extended &amp; Career Studies<br>
      420 Marlow Avenue, Suite 310<br>
      Halvern, CO 80999<br>
      555-014-2290<br>
      ecs@halvernridge.example<br>
      www.halvernridge.example/ecs
    </address>
    <svg class="bottom-swoosh" viewBox="0 0 418 40" preserveAspectRatio="none" aria-hidden="true">
      <path d="M0 0 C80 14 170 30 250 40 H0 Z" fill="var(--green)"/>
      <path d="M0 12 C70 24 140 34 205 40 H0 Z" fill="var(--blue)"/>
    </svg>
    <div class="web-address web-address--right">www.halvernridge.example/ecs</div>
  </section>

  <!-- Front cover -->
  <section class="page page--cover">
    <div class="color-bar"><span></span><span></span><span></span><span></span><span></span><span></span><span></span><span></span><span></span><span></span><span></span><span></span><span></span><span></span><span></span><span></span></div>
    <svg class="cover-art" viewBox="0 0 418 440" role="img" aria-label="Photo: a senior leader presenting to colleagues around a table in a bright meeting room">
      <defs>
        <linearGradient id="cover-photo" x1="0" y1="0" x2="1" y2="1">
          <stop offset="0" stop-color="#f6f6f6"/>
          <stop offset="0.45" stop-color="#e4e1de"/>
          <stop offset="0.7" stop-color="#9a8f88"/>
          <stop offset="1" stop-color="#2f3442"/>
        </linearGradient>
      </defs>
      <path d="M0 0 H418 V392 C300 360 150 315 0 285 Z" fill="url(#cover-photo)"/>
      <path d="M110 338 C240 362 340 388 418 398 V430 C330 412 230 380 110 338 Z" fill="var(--blue)"/>
      <path d="M190 374 C290 404 365 422 418 430 V438 C360 430 280 410 190 374 Z" fill="var(--green)"/>
    </svg>
    <div class="unit-mark cover-mark"><i></i>Extended &amp; Career Studies</div>
    <h1 class="cover-headline">
      <span class="line-1">You Are An</span>
      <span class="line-2">Aspiring Leader</span>
      <span class="line-3">With A Passion</span>
    </h1>
    <p class="cover-subtitle">Extended &amp; Career Studies</p>
    <div class="partner-mark cover-partner"><i></i>Brellow Regional Learning</div>
    <div class="web-address web-address--left">www.halvernridge.example/ecs</div>
  </section>

  <!-- Inside left -->
  <section class="page page--inside-left">
    <div class="color-bar"><span></span><span></span><span></span><span></span><span></span><span></span><span></span><span></span><span></span><span></span><span></span><span></span><span></span><span></span><span></span><span></span></div>

    <h2 class="tab tab--green" style="top:52px;width:167px;">Introduction</h2>
    <svg class="dot-arrow" style="left:23px;top:69px;fill:var(--green);" aria-hidden="true"><use href="#dot-arrow"/></svg>
    <div class="copy" style="top:70px;">
      <p>You are an aspiring leader with a passion for school reform and a dedication to becoming highly effective in supporting students in underrepresented groups.</p>
      <p>Through a partnership with Brellow Regional Learning, the Office of Extended &amp; Career Studies at Halvern Ridge University is offering a unique 32-credit hour principal licensure program that provides opportunities for licensure candidates to develop in-depth understanding of principal leadership with an emphasis on equity, language, and culture.</p>
    </div>

    <h2 class="tab tab--orange" style="top:141px;width:152px;">Philosophy</h2>
    <svg class="dot-arrow" style="left:23px;top:158px;fill:var(--green);" aria-hidden="true"><use href="#dot-arrow"/></svg>
    <div class="copy" style="top:159px;">
      <p>Make a tremendous impact on the success of students, teachers, schools and districts.</p>
      <p>We cultivate transformational leaders who are prepared to embrace exceptional opportunities and demanding challenges in today's schools with both zeal and resiliency. The program prepares candidates with not only the knowledge and skills to earn a principal license (CDE) but also with the experiences necessary to influence systems and people by leading successful schools in reaching organizational goals, including high performance and increases in student growth and achievement.</p>
    </div>

    <svg class="dot-arrow dot-arrow--small" style="left:56px;top:234px;fill:var(--teal);" aria-hidden="true"><use href="#dot-arrow"/></svg>
    <p class="copy" style="top:233px;">Work with experienced instructors to enhance self-awareness in order to more fully engage schools and communities in crucial conversations that value the language and culture of students and families as assets.</p>
    <svg class="dot-arrow dot-arrow--small" style="left:56px;top:266px;fill:var(--teal);" aria-hidden="true"><use href="#dot-arrow"/></svg>
    <p class="copy" style="top:265px;">Focus on building and maintaining relationships with school staff to develop strong support networks and maximize resources.</p>
    <svg class="dot-arrow dot-arrow--small" style="left:56px;top:290px;fill:var(--teal);" aria-hidden="true"><use href="#dot-arrow"/></svg>
    <p class="copy" style="top:290px;">Utilize technology as a means of empowerment for administrators, teachers, and students.</p>
    <svg class="dot-arrow dot-arrow--small" style="left:56px;top:307px;fill:var(--teal);" aria-hidden="true"><use href="#dot-arrow"/></svg>
    <p class="copy" style="top:307px;">Develop in-depth understanding about leadership roles and responsibilities, contemporary educational issues, and collaborations within and across communities.</p>
    <svg class="dot-arrow dot-arrow--small" style="left:56px;top:332px;fill:var(--teal);" aria-hidden="true"><use href="#dot-arrow"/></svg>
    <p class="copy" style="top:332px;">Raise a thorough awareness of the legal, financial and political dimensions of schools and school districts.</p>
    <svg class="dot-arrow dot-arrow--small" style="left:56px;top:357px;fill:var(--teal);" aria-hidden="true"><use href="#dot-arrow"/></svg>
    <p class="copy" style="top:357px;">Incorporate multiple perspectives, themes of equity and social justice, a focus on the needs and experiences of diverse children and youth, and implications for leadership in today's schools.</p>

    <h2 class="tab tab--green" style="top:393px;width:290px;">In Partnership with Brellow Regional Learning</h2>
    <svg class="dot-arrow" style="left:23px;top:412px;fill:var(--green);" aria-hidden="true"><use href="#dot-arrow"/></svg>
    <div class="copy" style="top:414px;">
      <p>Increasing the number of powerful leaders is essential to address the achievement gap in Halvern.</p>
      <p>HRU and Brellow Regional Learning collaborate to provide educators with leadership skills that have a profound impact on student opportunity, achievement and success in urban and diverse communities. Brellow Regional Learning is committed to principal autonomy and supports high caliber school leaders who are ready to lead.</p>
    </div>
    <p class="callout">Students who complete this cohort program will be provided with a preferred status in the candidacy for school leadership positions in Brellow Regional Learning.</p>

    <svg class="bottom-swoosh" viewBox="0 0 418 40" preserveAspectRatio="none" aria-hidden="true">
      <path d="M0 4 C150 22 300 32 418 36 V40 H0 Z" fill="var(--green)"/>
      <path d="M0 14 C90 28 190 36 290 40 H0 Z" fill="var(--blue)"/>
    </svg>
    <div class="web-address web-address--right">www.halvernridge.example/ecs</div>
  </section>

  <!-- Inside right -->
  <section class="page page--inside-right">
    <div class="color-bar"><span></span><span></span><span></span><span></span><span></span><span></span><span></span><span></span><span></span><span></span><span></span><span></span><span></span><span></span><span></span><span></span></div>

    <h2 class="tab tab--orange" style="top:52px;width:166px;">Program Layout</h2>
    <svg class="dot-arrow dot-arrow--small" style="left:54px;top:70px;fill:var(--teal);" aria-hidden="true"><use href="#dot-arrow"/></svg>
    <p class="copy" style="top:70px;">Candidates complete the 32-credit principal license program as part of a cohort of approximately 25 students.</p>
    <svg class="dot-arrow dot-arrow--small" style="left:54px;top:95px;fill:var(--teal);" aria-hidden="true"><use href="#dot-arrow"/></svg>
    <p class="copy" style="top:95px;">Courses combine face-to-face and online learning in hybrid courses delivered over four consecutive semesters (including summer semesters).</p>
    <svg class="dot-arrow dot-arrow--small" style="left:54px;top:127px;fill:var(--teal);" aria-hidden="true"><use href="#dot-arrow"/></svg>
    <p class="copy" style="top:127px;">Successful completion of course work and program requirements prepares candidates to apply for the initial principal license.</p>
    <svg class="dot-arrow dot-arrow--small" style="left:54px;top:154px;fill:var(--teal);" aria-hidden="true"><use href="#dot-arrow"/></svg>
    <p class="copy" style="top:154px;">Face-to-face sessions:</p>

    <ul class="sessions">
      <li><b>1 week-long induction:</b> June 24-28, 2013</li>
      <li><b>2 fall term weekends (Friday evening &amp; all-day Saturday):</b> September 13-14 &amp; November 22-23, 2013</li>
      <li><b>2 spring term weekends (Friday evening &amp; all-day Saturday):</b> February 14-15, 2014 &amp; April 11-12, 2014</li>
      <li><b>1 final day</b> - July 26, 2014</li>
    </ul>

    <h2 class="tab tab--green" style="top:269px;width:134px;">Practical</h2>
    <svg class="dot-arrow" style="left:28px;top:287px;fill:var(--orange);" aria-hidden="true"><use href="#dot-arrow"/></svg>
    <p class="copy" style="top:288px;">Engage in school-based research projects that focus on the everyday tasks and challenges that face today's principals. Course and clinical practice experiences are integrated throughout the program and principal candidates may be able to use their own school as a clinical-practice site.</p>

    <h2 class="tab tab--orange" style="top:350px;width:168px;">HRU Faculty</h2>
    <svg class="dot-arrow" style="left:28px;top:369px;fill:var(--orange);" aria-hidden="true"><use href="#dot-arrow"/></svg>
    <p class="copy" style="top:371px;">Study with expert faculty who are engaged in education at the state, national and international levels. Faculty collaborate with BRL principals and district leaders to form an instructional team that expands your professional horizons and connects you to best practices and the newest research emerging from innovative school and district reform.</p>

    <h2 class="tab tab--green" style="top:439px;width:138px;">Affordable</h2>
    <svg class="dot-arrow" style="left:28px;top:458px;fill:var(--orange);" aria-hidden="true"><use href="#dot-arrow"/></svg>
    <p class="price"><strong>$349</strong> per credit or <strong>$11,168</strong> for <strong>32</strong> credits<br>(plus hybrid course fees)</p>

    <div class="info-box">
      <h3>Information Session</h3>
      <p>Join us for the BRL Principal Cohort Information Session that will be held in April. Meet HRU faculty and BRL representatives and network with your colleagues. For more information please contact ecs@halvernridge.example</p>
    </div>

    <aside class="apply">
      <h2>Apply</h2>
      <p>All applicants must hold at least a bachelor's degree and a teaching or special services license; we recommend approximately three years of post- teacher licensure experience in the field of education.</p>
      <p>The ARC program seeks students who possess:</p>
      <ul>
        <li><svg aria-hidden="true"><use href="#line-arrow"/></svg>High intellectual ability</li>
        <li><svg aria-hidden="true"><use href="#line-arrow"/></svg>Strong academic backgrounds</li>
        <li><svg aria-hidden="true"><use href="#line-arrow"/></svg>Clear leadership potential</li>
      </ul>
      <p><b>Application Deadline:</b><br>April 15, 2013</p>
      <p>Interested principal licensure candidates will apply either for the MA or EdS degree programs, although finishing the degree requirements is optional after students have completed the 32-credit licensure program. If you do not have a previous graduate degree, you may complete 9 additional semester credits and a brief paper to earn an MA degree in Administrative Leadership and Policy Studies. If you have a previous master's degree, you may complete 9 additional semester credits and a brief paper to earn a EdS degree in Administrative Leadership and Policy Studies.</p>
      <p><b>For application instructions go to:</b><br><span class="link">http://www.halvernridge.example/teaching/apply/leadership-policy-studies</span></p>
    </aside>

    <svg class="bottom-swoosh" viewBox="0 0 418 40" preserveAspectRatio="none" aria-hidden="true">
      <path d="M0 18 C120 30 260 36 418 30 V40 H0 Z" fill="var(--green)"/>
      <path d="M0 22 C80 32 160 38 230 40 H0 Z" fill="var(--blue)"/>
    </svg>
    <div class="web-address web-address--left">www.halvernridge.example/ecs</div>
  </section>

</main>
</body>
</html>
```